Redesign of iOS App Lumo Tutor

Redesign of existing App Lumo Tutor, an app that helps learning Japanese Kanjis, Hiragana, Katakana.

The functionallity should remain the same as today: the app is free, you may download it at the app store. But: I like the design of my other apps better ;)

Target Market(s)

Students learning Japanese

Industry/Entity Type

Teacher

Font styles to use
Sans Serif

Requirements
Must have
• Lumo Tutor has 7 main screens, all screens has to be designed for iPhone and iPad: Main, Settings, Reading Tests, Writing Tests, Game, Paper Mode, Search
Nice to have
• I like the logo as it is today

```html
<!DOCTYPE html>
<html lang="en">
<head>
<meta charset="utf-8">
<title>Lumo Tutor – App Screens</title>
<link rel="stylesheet" href="https://fonts.googleapis.com/css2?family=Roboto:wght@400;500&family=Noto+Sans+JP:wght@400;500&display=swap">
<style>
:root{
  --bg:#38ae8e;
  --blue:#0c62cf;
  --blue-text:#2b7ee0;
  --screen:#ececec;
  --white:#ffffff;
  --ink:#1a1a1a;
  --grey-text:#9a9a9a;
  --line:#d5d5d5;
  --red:#f2604a;
  --teal:#1cc1ac;
  --orange:#f08a2a;
  --btn:#d6d6d6;
  --yellow:#fde58a;
  --yellow-line:#e6c94d;
}
*{box-sizing:border-box;margin:0;padding:0}
html,body{width:1200px;height:1200px;overflow:hidden;background:var(--bg)}
body{font-family:"Roboto",sans-serif;color:var(--ink)}
.stage{position:absolute;left:0;top:0;width:1500px;height:1500px;transform:scale(.8);transform-origin:0 0}
.phone{position:absolute;width:311px;height:552px;background:var(--screen);overflow:hidden;box-shadow:0 2px 6px rgba(0,0,0,.12)}
.jp{font-family:"Noto Sans JP",sans-serif}
.abs{position:absolute}

/* top chrome */
.status{position:absolute;left:0;top:0;width:100%;height:20px;background:var(--blue);color:var(--white);font-size:8px;line-height:16px}
.status .l{position:absolute;left:5px}
.status .c{position:absolute;left:0;right:0;text-align:center}
.status .r{position:absolute;right:6px;display:flex;align-items:center;gap:4px}
.status .batt{width:15px;height:6px;border:1px solid #fff;background:linear-gradient(90deg,#fff 80%,transparent 80%)}
.navbar{position:absolute;left:0;top:20px;width:100%;height:28px;background:var(--blue);color:var(--white)}
.navbar .home{position:absolute;left:8px;top:6px}
.navbar .brand{position:absolute;left:0;right:0;top:6px;text-align:center;font-size:12px;font-weight:500}
.navbar .next{position:absolute;right:6px;top:5px}

/* stats strip */
.stats{position:absolute;left:0;top:48px;width:100%;height:46px;background:var(--white);display:flex;border-bottom:1px solid #e2e2e2}
.stats .cell{flex:1;text-align:center;position:relative;padding-top:7px}
.stats .cell+.cell::before{content:"";position:absolute;left:0;top:8px;bottom:8px;border-left:1px solid #e4e4e4}
.stats .lbl{font-size:11px}
.stats .val{font-size:15px;margin-top:1px}
.stats .sub{font-size:10px;margin-top:1px}
.c-red{color:var(--red)} .c-teal{color:var(--teal)} .c-blue{color:var(--blue-text)} .c-gold{color:#f4b63a} .c-ink{color:var(--ink)}

.title{position:absolute;left:0;right:0;text-align:center;color:var(--blue-text);font-size:22px}
.subtitle{position:absolute;left:0;right:0;text-align:center;color:var(--grey-text);font-size:13px}
.star{position:absolute}

/* writing pad */
.pad{position:absolute;left:17px;top:192px;width:277px;height:277px;background:var(--white);border:1px solid #9a9a9a}
.pad::before{content:"";position:absolute;left:50%;top:0;bottom:0;border-left:1px solid #cfcfcf}
.pad::after{content:"";position:absolute;top:50%;left:0;right:0;border-top:1px solid #cfcfcf}
.strokes{position:absolute;inset:18px;z-index:1}
.answer-bar{position:absolute;background:#e8e8e8;border:1px solid #d2d2d2;border-radius:3px;display:flex;align-items:center;justify-content:center}

/* list */
.search{position:absolute;left:7px;top:52px;width:265px;height:24px;border:1px solid var(--white);border-radius:12px;background:var(--blue);color:#a9c8f3;font-size:13px;line-height:22px;padding-left:30px}
.search svg{position:absolute;left:9px;top:5px}
.help{position:absolute;left:279px;top:53px;width:24px;height:24px;border-radius:50%;background:var(--white);color:var(--blue);font-weight:500;font-size:15px;text-align:center;line-height:24px}
.row{position:absolute;left:7px;width:296px;height:52px;background:var(--white);box-shadow:0 1px 2px rgba(0,0,0,.08)}
.row .sq{position:absolute;left:0;top:0;width:49px;height:52px;color:var(--white);font-size:28px;text-align:center;line-height:50px}
.row .kana{position:absolute;left:58px;top:10px;font-size:14px}
.row .dots{position:absolute;left:58px;top:32px;font-size:9px;letter-spacing:1px;color:#c2c2c2}
.row .type{position:absolute;left:117px;top:11px;font-size:14px}
.row .k{position:absolute;left:229px;top:11px;font-size:14px}
.row .fav{position:absolute;left:252px;top:8px;height:36px;border-left:1px solid #e3e3e3;padding-left:8px;padding-top:7px}

.popup{position:absolute;left:137px;top:335px;width:167px;height:211px;background:var(--white);box-shadow:0 1px 4px rgba(0,0,0,.25);border-radius:3px}
.popup .head{height:30px;background:var(--blue);color:var(--white);font-size:13px;text-align:center;line-height:30px;border-radius:3px 3px 0 0}
.popup .sect{position:absolute;left:6px;right:6px;font-size:11px;color:var(--grey-text);display:flex;align-items:center;gap:5px}
.popup .sect::after{content:"";flex:1;border-top:1px solid #d8d8d8}
.popup .sw{position:absolute;top:71px;width:24px;height:24px;border-radius:3px}
.popup .select{position:absolute;left:7px;right:7px;top:178px;height:22px;border:1px solid #cfcfcf;border-radius:3px;font-size:11px;line-height:20px;padding-left:6px}
.popup .select svg{position:absolute;right:5px;top:7px}

/* small kanji card */
.kcard{position:absolute;left:130px;top:105px;width:51px;height:51px;background:#f6f6f6;border:1px solid #d8d8d8;font-size:26px;text-align:center;line-height:49px}
.pad-btn{position:absolute;top:10px;z-index:2;width:20px;height:20px;border-radius:50%;background:#c8c8c8;color:var(--white);text-align:center;font-size:13px;line-height:19px}
.back{position:absolute;width:22px;height:22px;border-radius:50%;background:#dedede;text-align:center;line-height:20px;font-size:14px;color:#444}
.choice{position:absolute;top:486px;width:51px;height:51px;border-radius:3px;font-size:28px;text-align:center;line-height:48px}

/* answer grid */
.tile{position:absolute;width:89px;height:95px;border:1px solid #d3d3d3;border-radius:2px;background:#ededed;display:flex;align-items:center;justify-content:center;font-size:15px}
.tile.wrong{background:var(--red);border-color:var(--red);color:var(--white)}
.tile.right{background:var(--teal);border-color:var(--teal);color:var(--white)}
.tile.faded{color:#c8c8c8;background:#efefef;border-color:#e0e0e0}
.tile.grey{background:#dcdcdc;border-color:#cdcdcd}
.power{position:absolute;top:488px;width:51px;height:51px;border:1px solid var(--yellow-line);border-radius:4px;background:var(--yellow);text-align:center;font-size:13px;line-height:14px;padding-top:9px}
.power small{display:block;font-size:10px}
.power.dim{background:#fdf1c6;color:#9a8d5c;border-color:#f0dd95}

/* settings */
.set-label{position:absolute;left:7px;right:7px;font-size:15px;display:flex;align-items:center;gap:8px}
.set-label::after{content:"";flex:1;border-top:1px solid #9a9a9a}
.opt{position:absolute;height:34px;background:var(--btn);border-radius:2px;font-size:13px;text-align:center;line-height:34px;color:#333}
.opt.on{background:var(--orange);color:var(--white)}
.thanks{position:absolute;left:0;right:0;text-align:center;font-size:11px;color:#999;line-height:16px}
</style>
</head>
<body>
<div class="stage">

<!-- ============ Writing test ============ -->
<section class="phone" style="left:154px;top:140px" aria-label="Writing test">
  <div class="status"><span class="l">●●●○○ Lumo</span><span class="c">12:37 pm</span><span class="r">80% <span class="batt"></span></span></div>
  <div class="navbar">
    <svg class="home" width="17" height="15" viewBox="0 0 17 15"><path d="M8.5 1 1 7.5h2.2V14h3.8V9.5h3V14h3.8V7.5H16z" fill="#fff"/></svg>
    <div class="brand">Lumo</div>
    <svg class="next" width="10" height="18" viewBox="0 0 10 18"><path d="M2 2l6 7-6 7" stroke="#fff" stroke-width="1.6" fill="none"/></svg>
  </div>
  <div class="stats">
    <div class="cell"><div class="lbl c-ink">Remaining</div><div class="val c-ink">102</div></div>
    <div class="cell"><div class="lbl c-red">Wrong</div><div class="val c-red">1</div></div>
    <div class="cell"><div class="lbl c-teal">Correct</div><div class="val c-teal">0</div></div>
  </div>
  <div class="title" style="top:118px">Fire</div>
  <div class="subtitle" style="top:149px">Fire</div>
  <svg class="star" style="left:273px;top:108px" width="20" height="20" viewBox="0 0 24 24"><path d="M12 2.5l2.9 6.3 6.8.7-5.1 4.6 1.5 6.7L12 17.3l-6.1 3.5 1.5-6.7L2.3 9.5l6.8-.7z" fill="none" stroke="#333" stroke-width="1.3"/></svg>
  <div class="pad">
    <div class="strokes" role="img" aria-label="Handwritten strokes of the kanji for fire drawn by the learner" style="background:linear-gradient(135deg,rgba(255,255,255,0) 0%,rgba(0,0,0,.06) 100%)"></div>
  </div>
  <div class="answer-bar jp" style="left:17px;top:493px;width:277px;height:51px;font-size:28px">火</div>
</section>

<!-- ============ Search ============ -->
<section class="phone" style="left:594px;top:140px" aria-label="Search">
  <div class="status"><span class="l">●●●○○ Lumo</span><span class="c">12:37 pm</span><span class="r">80% <span class="batt"></span></span></div>
  <div class="navbar">
    <svg class="home" width="17" height="15" viewBox="0 0 17 15"><path d="M8.5 1 1 7.5h2.2V14h3.8V9.5h3V14h3.8V7.5H16z" fill="#fff"/></svg>
    <div class="brand">Lumo</div>
    <svg class="next" width="10" height="18" viewBox="0 0 10 18"><path d="M2 2l6 7-6 7" stroke="#fff" stroke-width="1.6" fill="none"/></svg>
  </div>
  <div class="status" style="top:48px;height:38px"></div>
  <div class="search"><svg width="12" height="12" viewBox="0 0 12 12"><circle cx="5" cy="5" r="3.6" stroke="#fff" stroke-width="1.6" fill="none"/><path d="M7.8 7.8 11 11" stroke="#fff" stroke-width="1.8"/></svg>Search</div>
  <div class="help">?</div>

  <div class="row" style="top:87px"><div class="sq jp" style="background:#26c6b0">あ</div><div class="kana" style="color:#26c6b0">a</div><div class="dots">●●●</div><div class="type">Hiragana</div><div class="k">K</div><div class="fav"><svg width="24" height="24" viewBox="0 0 24 24"><path d="M12 2.5l2.9 6.3 6.8.7-5.1 4.6 1.5 6.7L12 17.3l-6.1 3.5 1.5-6.7L2.3 9.5l6.8-.7z" fill="none" stroke="#bbb" stroke-width="1"/></svg></div></div>
  <div class="row" style="top:145px"><div class="sq jp" style="background:#f2614a">あ</div><div class="kana" style="color:#f2614a">i</div><div class="dots">●●●</div><div class="type">Hiragana</div><div class="k">K</div><div class="fav"><svg width="24" height="24" viewBox="0 0 24 24"><path d="M12 2.5l2.9 6.3 6.8.7-5.1 4.6 1.5 6.7L12 17.3l-6.1 3.5 1.5-6.7L2.3 9.5l6.8-.7z" fill="none" stroke="#bbb" stroke-width="1"/></svg></div></div>
  <div class="row" style="top:203px"><div class="sq jp" style="background:#3f9ee8">あ</div><div class="kana" style="color:#3f9ee8">u</div><div class="dots">●●●</div><div class="type">Hiragana</div><div class="k">K</div><div class="fav"><svg width="24" height="24" viewBox="0 0 24 24"><path d="M12 2.5l2.9 6.3 6.8.7-5.1 4.6 1.5 6.7L12 17.3l-6.1 3.5 1.5-6.7L2.3 9.5l6.8-.7z" fill="none" stroke="#bbb" stroke-width="1"/></svg></div></div>
  <div class="row" style="top:261px"><div class="sq jp" style="background:#b0477e">あ</div><div class="kana" style="color:#b0477e">e</div><div class="dots">●●●</div><div class="type">Hiragana</div><div class="k">K</div><div class="fav"><svg width="24" height="24" viewBox="0 0 24 24"><path d="M12 2.5l2.9 6.3 6.8.7-5.1 4.6 1.5 6.7L12 17.3l-6.1 3.5 1.5-6.7L2.3 9.5l6.8-.7z" fill="none" stroke="#bbb" stroke-width="1"/></svg></div></div>
  <div class="row" style="top:319px"><div class="sq jp" style="background:#7e55b0">あ</div><div class="kana" style="color:#7e55b0">o</div><div class="dots">●●●</div><div class="type">Hiragana</div></div>
  <div class="row" style="top:377px"><div class="sq jp" style="background:#4d7fa8">あ</div><div class="kana" style="color:#4d7fa8">ka</div><div class="dots">●●●</div><div class="type">Hiragana</div></div>
  <div class="row" style="top:435px"><div class="sq jp" style="background:#3d9a84">あ</div><div class="kana" style="color:#3d9a84">ga</div><div class="dots">●●●</div><div class="type">Hiragana</div></div>
  <div class="row" style="top:493px"><div class="sq jp" style="background:#c46ac0">あ</div><div class="kana" style="color:#c46ac0">ki</div><div class="dots">●●●</div><div class="type">Hiragana</div></div>

  <div class="popup">
    <div class="head">Practice Writing</div>
    <div class="sect" style="top:44px">Mark 30848 Tests</div>
    <div class="sw" style="left:11px;background:#8e8e8e"></div>
    <div class="sw" style="left:51px;background:#f2604a"></div>
    <div class="sw" style="left:90px;background:#3f9ee8"></div>
    <div class="sw" style="left:130px;background:#1cc1ac"></div>
    <div class="sect" style="top:109px">Mark 2136 Kanjis</div>
    <svg class="abs" style="left:40px;top:131px" width="32" height="32" viewBox="0 0 24 24"><path d="M12 2.5l2.9 6.3 6.8.7-5.1 4.6 1.5 6.7L12 17.3l-6.1 3.5 1.5-6.7L2.3 9.5l6.8-.7z" fill="none" stroke="#222" stroke-width="1"/></svg>
    <svg class="abs" style="left:90px;top:131px" width="32" height="32" viewBox="0 0 24 24"><path d="M12 2.5l2.9 6.3 6.8.7-5.1 4.6 1.5 6.7L12 17.3l-6.1 3.5 1.5-6.7L2.3 9.5l6.8-.7z" fill="#111"/></svg>
    <div class="select">2278 entries found<svg width="10" height="6" viewBox="0 0 10 6"><path d="M0 0h10L5 6z" fill="#aaa"/></svg></div>
  </div>
</section>

<!-- ============ Paper mode writing ============ -->
<section class="phone" style="left:1034px;top:140px" aria-label="Paper mode writing test">
  <div class="status"><span class="l">●●●○○ Lumo</span><span class="c">12:37 pm</span><span class="r">80% <span class="batt"></span></span></div>
  <div class="navbar"><div class="brand">Lumo</div></div>
  <div class="stats">
    <div class="cell"><div class="lbl c-red">Wrong</div><div class="val c-red">0</div></div>
    <div class="cell"><div class="lbl">&nbsp;</div><div class="val c-blue">0</div></div>
    <div class="cell"><div class="lbl c-teal">Correct</div><div class="val c-teal">1</div></div>
  </div>
  <div class="kcard jp">江</div>
  <div class="subtitle" style="top:164px;font-size:14px">Creek</div>
  <div class="pad">
    <div class="pad-btn" style="left:8px">×</div>
    <div class="pad-btn" style="right:8px">›</div>
    <div class="strokes" role="img" aria-label="Handwritten strokes of the kanji for creek drawn by the learner" style="background:linear-gradient(135deg,rgba(255,255,255,0) 0%,rgba(0,0,0,.06) 100%)"></div>
  </div>
  <div class="back" style="left:18px;top:500px">‹</div>
  <div class="choice jp" style="left:175px;background:#d9f5ef;border:1px solid #62d3bf">江</div>
  <div class="choice jp" style="left:242px;background:#dbeafb;border:1px solid #5aa3ec">汢</div>
</section>

<!-- ============ Reading test ============ -->
<section class="phone" style="left:154px;top:800px" aria-label="Reading test">
  <div class="status"><span class="l">●●●○○ Lumo</span><span class="c">12:37 pm</span><span class="r">80% <span class="batt"></span></span></div>
  <div class="navbar">
    <svg class="home" width="17" height="15" viewBox="0 0 17 15"><path d="M8.5 1 1 7.5h2.2V14h3.8V9.5h3V14h3.8V7.5H16z" fill="#fff"/></svg>
    <div class="brand">Lumo</div>
  </div>
  <div class="stats">
    <div class="cell"><div class="lbl c-ink">Remaining</div><div class="val c-ink">102</div></div>
    <div class="cell"><div class="lbl c-red">Wrong</div><div class="val c-red">1</div></div>
    <div class="cell"><div class="lbl c-teal">Correct</div><div class="val c-teal">0</div></div>
  </div>
  <div class="title jp" style="top:110px;font-size:32px">名</div>
  <div class="subtitle" style="top:153px">Fire</div>
  <svg class="star" style="left:273px;top:108px" width="20" height="20" viewBox="0 0 24 24"><path d="M12 2.5l2.9 6.3 6.8.7-5.1 4.6 1.5 6.7L12 17.3l-6.1 3.5 1.5-6.7L2.3 9.5l6.8-.7z" fill="none" stroke="#333" stroke-width="1.3"/></svg>
  <div class="tile" style="left:17px;top:187px">Seven</div>
  <div class="tile wrong" style="left:111px;top:187px">Person</div>
  <div class="tile" style="left:205px;top:187px">Long</div>
  <div class="tile right" style="left:17px;top:287px">Name</div>
  <div class="tile" style="left:111px;top:287px">Come</div>
  <div class="tile" style="left:205px;top:287px">Many</div>
  <div class="tile" style="left:17px;top:387px">Write</div>
  <div class="tile" style="left:111px;top:387px">In</div>
  <div class="tile" style="left:205px;top:387px">Station</div>
  <div class="answer-bar jp" style="left:17px;top:508px;width:132px;height:36px;font-size:22px">名</div>
  <div class="answer-bar" style="left:161px;top:508px;width:132px;height:36px;font-size:14px">Skip&nbsp;<span style="font-size:18px">»</span></div>
</section>

<!-- ============ Game ============ -->
<section class="phone" style="left:594px;top:800px" aria-label="Game">
  <div class="status"><span class="l">●●●○○ Lumo</span><span class="c">12:37 pm</span><span class="r">80% <span class="batt"></span></span></div>
  <div class="navbar"><div class="brand">Lumo</div></div>
  <div class="stats" style="height:66px">
    <div class="cell"><div class="lbl c-red">Lives</div><div class="val c-red">0</div><div class="sub c-red">Level N5</div></div>
    <div class="cell"><div class="lbl c-blue">Score</div><div class="val c-blue">0</div><div class="sub c-blue">Highscore: 8</div></div>
    <div class="cell"><div class="lbl c-gold">Coins</div><div class="val c-gold">12</div></div>
  </div>
  <div class="title" style="top:132px">Fire</div>
  <div class="tile faded" style="left:17px;top:179px">Seven</div>
  <div class="tile faded" style="left:111px;top:179px">Person</div>
  <div class="tile grey" style="left:205px;top:179px">Long</div>
  <div class="tile grey" style="left:17px;top:279px">Name</div>
  <div class="tile faded" style="left:111px;top:279px">Come</div>
  <div class="tile faded" style="left:205px;top:279px">Many</div>
  <div class="tile grey" style="left:17px;top:379px">Write</div>
  <div class="tile grey" style="left:111px;top:379px">In</div>
  <div class="tile faded" style="left:205px;top:379px">Station</div>
  <div class="back" style="left:18px;top:503px">‹</div>
  <div class="power" style="left:55px">Level<br>up</div>
  <div class="power dim" style="left:117px">Live+<small>-24</small></div>
  <div class="power" style="left:180px">Split<small>-8</small></div>
  <div class="power" style="left:242px">Hint<small>-4</small></div>
</section>

<!-- ============ Settings ============ -->
<section class="phone" style="left:1034px;top:800px" aria-label="Settings">
  <div class="status"><span class="l">●●●○○ Lumo</span><span class="c">12:37 pm</span><span class="r">80% <span class="batt"></span></span></div>
  <div class="navbar">
    <svg class="home" width="17" height="15" viewBox="0 0 17 15"><path d="M8.5 1 1 7.5h2.2V14h3.8V9.5h3V14h3.8V7.5H16z" fill="#fff"/></svg>
    <div class="brand">Lumo</div>
  </div>
  <div class="set-label" style="top:59px">Group Tests by</div>
  <div class="opt on" style="left:7px;top:87px;width:145px">JLPT Level</div>
  <div class="opt" style="left:159px;top:87px;width:145px">School Year</div>
  <div class="set-label" style="top:132px">Size of Answer Grid</div>
  <div class="opt on" style="left:7px;top:160px;width:145px">3 * 3</div>
  <div class="opt" style="left:159px;top:160px;width:145px">4 * 4</div>
  <div class="set-label" style="top:205px">Show Meaning in Tests</div>
  <div class="opt" style="left:7px;top:233px;width:94px">Never</div>
  <div class="opt on" style="left:108px;top:233px;width:94px">Classic</div>
  <div class="opt" style="left:209px;top:233px;width:95px">Always</div>
  <div class="set-label" style="top:278px">Show Pattern in Writing Tests</div>
  <div class="opt" style="left:7px;top:306px;width:94px">Never</div>
  <div class="opt on" style="left:108px;top:306px;width:94px">First Tests</div>
  <div class="opt" style="left:209px;top:306px;width:95px">Always</div>
  <div class="set-label" style="top:351px">Tests used in Game</div>
  <div class="opt" style="left:7px;top:379px;width:94px">Meaning</div>
  <div class="opt" style="left:108px;top:379px;width:94px">Reading</div>
  <div class="opt on" style="left:209px;top:379px;width:95px">Both</div>
  <div class="set-label" style="top:424px">Feedback</div>
  <div class="opt" style="left:7px;top:452px;width:145px">Rate</div>
  <div class="opt" style="left:159px;top:452px;width:145px">E-Mail</div>
  <div class="thanks" style="top:502px">Many thanks to wordlex.net and strokebase.org<br>Many thanks to wordlex.net and strokebase.org</div>
</section>

</div>
</body>
</html>
```